We need a business card design for a Dubai based company .

We need a business card for a Dubai based company called "Zernova Hookah Essentials Trading LLC". We mainly import Flavoured Tobacco products and Charcoal which is used for smoking in a Hookah/Shisha and distribute to the wholesalers and retailers. Logo file is attached herewith.

```html
<!DOCTYPE html>
<html lang="en">
<head>
<meta charset="utf-8">
<title>Zernova Business Card</title>
<link rel="stylesheet" href="https://fonts.googleapis.com/css2?family=Montserrat:wght@400;500;600&display=swap">
<style>
  :root {
    --stage: #2b2b2f;
    --card: #1b1a1c;
    --red: #c9262c;
    --white: #f4f4f4;
    --muted: #d9d9d9;
  }
  * { box-sizing: border-box; margin: 0; padding: 0; }
  html, body { width: 1200px; height: 786px; overflow: hidden; }
  body {
    background: var(--stage);
    font-family: "Montserrat", Arial, sans-serif;
    display: flex;
    align-items: center;
    justify-content: center;
    gap: 40px;
  }
  .card {
    width: 540px;
    height: 309px;
    background: var(--card);
    border: 6px solid var(--red);
    position: relative;
    display: flex;
    align-items: center;
  }
  .brand {
    display: flex;
    flex-direction: column;
    align-items: center;
    gap: 8px;
  }
  .brand-name {
    display: flex;
    align-items: center;
    gap: 10px;
    color: var(--white);
    font-weight: 500;
    letter-spacing: 0.18em;
    text-transform: uppercase;
    white-space: nowrap;
  }
  .brand-mark {
    width: 14px;
    height: 14px;
    border: 2px solid var(--red);
  }
  .brand-tagline {
    color: var(--red);
    font-weight: 500;
    letter-spacing: 0.2em;
    text-transform: uppercase;
    white-space: nowrap;
  }
  /* Contact side */
  .card-front .brand { width: 250px; flex: none; }
  .card-front .brand-name { font-size: 26px; }
  .card-front .brand-tagline { font-size: 6.5px; }
  .divider {
    width: 1px;
    height: 150px;
    background: var(--red);
    margin: 0 26px 0 4px;
    flex: none;
  }
  .contact { color: var(--muted); font-size: 11.5px; line-height: 1.55; }
  .contact .name {
    color: var(--red);
    font-weight: 600;
    font-size: 15px;
    letter-spacing: 0.03em;
    text-transform: uppercase;
  }
  .contact .role { text-transform: uppercase; letter-spacing: 0.04em; margin-bottom: 2px; }
  .contact-line { display: flex; align-items: center; gap: 6px; }
  .contact-line svg { width: 10px; height: 10px; flex: none; }
  /* Logo side */
  .card-back { justify-content: center; }
  .card-back .brand-name { font-size: 38px; }
  .card-back .brand-tagline { font-size: 9px; }
</style>
</head>
<body>
  <section class="card card-front">
    <div class="brand">
      <div class="brand-name"><span class="brand-mark"></span>Zernova</div>
      <div class="brand-tagline">Hookah Essentials Trading LLC</div>
    </div>
    <div class="divider"></div>
    <div class="contact">
      <p class="name">Daniel Harlow</p>
      <p class="role">Director</p>
      <p>1470 Meridian Avenue,</p>
      <p>Suite 318 Dayton, OH</p>
      <p class="contact-line">
        <svg viewBox="0 0 10 10"><path d="M2 1 L4 1 L4.6 3 L3.4 3.8 Q4.4 5.8 6.2 6.6 L7 5.4 L9 6 L9 8 Q8.6 9 7.6 9 Q1 8 1 2.4 Q1 1.2 2 1 Z" fill="var(--red)"/></svg>
        5550142786
      </p>
      <p class="contact-line">
        <svg viewBox="0 0 10 10"><rect x="1" y="2" width="8" height="6" fill="none" stroke="var(--red)" stroke-width="1"/><path d="M1 2 L5 5.5 L9 2" fill="none" stroke="var(--red)" stroke-width="1"/></svg>
        info@zernova.com
      </p>
      <p class="contact-line">
        <svg viewBox="0 0 10 10"><circle cx="5" cy="5" r="4" fill="none" stroke="var(--red)" stroke-width="1"/><ellipse cx="5" cy="5" rx="1.8" ry="4" fill="none" stroke="var(--red)" stroke-width="0.8"/><path d="M1 5 H9" stroke="var(--red)" stroke-width="0.8"/></svg>
        www.zernova.com
      </p>
    </div>
  </section>

  <section class="card card-back">
    <div class="brand">
      <div class="brand-name"><span class="brand-mark"></span>Zernova</div>
      <div class="brand-tagline">Hookah Essentials Trading LLC</div>
    </div>
  </section>
</body>
</html>
```